Visitenkarten-Design für modernes Industrieunternehmen
Zielgruppe
Wir stellen loses Füllmaterial (Schaumstoff-sticks, Latex-sticks und Visco-sticks) für Kopfkissen und Polstermöbel her. Auch Füllungen für Gartenauflagen sind in unserem Repertoire.
Aufgabenstellung
Wir liefern nicht an Endkunden, sondern nur an andere Unternehmen. Die Visitenkarte soll daher eine gewisse Seriösität ausstrahlen, aber trotzdem ins Auge fallen.

```html
<!DOCTYPE html>
<html lang="de">
<head>
<meta charset="utf-8">
<title>Polvera – Visitenkarte</title>
<link rel="stylesheet" href="https://fonts.googleapis.com/css2?family=Arimo:wght@400;700&family=Tinos&display=swap">
<style>
  :root {
    --bg: #c9d1d6;
    --card: #f7f8f8;
    --brand-blue: #1f66b3;
    --rule-teal: #1f8fb8;
    --ink: #2b2f33;
    --photo-light: #eef0ee;
    --photo-mid: #d9dcd8;
    --photo-warm: #b3aa9c;
  }
  * { box-sizing: border-box; margin: 0; padding: 0; }
  html, body { width: 1200px; height: 857px; overflow: hidden; }
  body {
    background: var(--bg);
    display: flex;
    align-items: center;
    justify-content: center;
    gap: 60px;
  }
  .card {
    width: 520px;
    height: 336px;
    background: var(--card);
    position: relative;
    box-shadow: 0 6px 18px rgba(0,0,0,0.18);
    overflow: hidden;
  }
  .brand-name {
    position: absolute;
    top: 40px;
    right: 44px;
    font-family: "Arimo", sans-serif;
    font-weight: 700;
    font-size: 30px;
    line-height: 1;
    color: var(--brand-blue);
    letter-spacing: 1px;
  }
  .rule {
    position: absolute;
    top: 100px;
    left: 58px;
    right: 32px;
    border-top: 2px solid var(--rule-teal);
  }
  .address {
    position: absolute;
    top: 160px;
    left: 70px;
    font-family: "Arimo", sans-serif;
    font-style: normal;
    font-size: 17px;
    line-height: 24px;
    color: var(--ink);
  }
  .contact {
    position: absolute;
    bottom: 34px;
    left: 88px;
    right: 24px;
    font-family: "Tinos", serif;
    font-size: 13px;
    color: var(--ink);
    white-space: nowrap;
  }
  .card-back .photo {
    position: absolute;
    inset: 0;
    background:
      radial-gradient(ellipse at 70% 45%, var(--photo-warm) 0%, rgba(179,170,156,0) 40%),
      linear-gradient(160deg, var(--photo-light) 0%, var(--photo-mid) 55%, var(--photo-warm) 100%);
  }
</style>
</head>
<body>
  <section class="card card-front">
    <span class="brand-name">Polvera</span>
    <div class="rule"></div>
    <address class="address">
      Polvera GmbH<br>
      Ahornweg 12<br>
      51379 Feldbach
    </address>
    <p class="contact">+49 (0) 30 55 / 48 17 62 | info@polvera.info | http://www.polvera.info</p>
  </section>

  <section class="card card-back">
    <div class="photo" role="img" aria-label="Foto: Hand greift in loses weißes Schaumstoff-Füllmaterial in einem geöffneten Kopfkissen"></div>
  </section>
</body>
</html>
```